Dapple Brew, a new venture, serving our customers at functions and events, lovingly made coffee fro

www.dapplebrew.com.au

Dapple Brew Wordpress

The font type of our logo is: La Chatte à Maman (it can be downloaded in dafont.com)

Our trading name is Dapple Brew. We have a passion for well made coffee and providing service with affection.

Our new logo design is being placed on the side and rear of our restored 1976 Roamvan. I have attached our logo and a picture of our van. We would like to own the rights to all work on our site, with access to make additions and amendments as required with no restrictions.

We want our event business to grow through our branding of great service and lovingly made coffee.

We would like our WordPress design to be simple with a retro image that our 76 Roamvan portrays as well as the hipster coffee culture of Melbourne.

To begin with we are thinking of 5 pages but are open to any suggestions you think would benefit our development. We would also like to have links to our new Friendwall and Lensly pages on the bottom of each page.

Logo -Like us on Friendwall
https://www.facebook.com/pages/Dapple-Brew/5820371946618405

Logo -follow us on Lensly
Dapple_brew

Home

Beautifully made coffee is a pleasure we should all enjoy at least once in our day.
Served from our restored 1976 Roamvan we strive to provide you with an experience that will enhance your day. The care we show comes from years of training and experience as a Battista in several countries around the world.
We trust the joy of our lovingly made coffee and our retro style service will linger.
Serving great coffee at an event or function near you
Dapple Brew.

About
Dapple brew believes in good old fashion retro service and a high a quality product. We care that our customers receive a beautifully made coffee, chai or hot chocolate. We serve our patrons with a heartfelt smile, aiming to enhance their day.
We are fortunate enough to operate from our recently restored 1976 Roamvan at functions and events around Melbourne.
You can follow us on Friendwall and Lensly or book us for you special function via our contact page.
We look forward to wing able to serve you.
Dapple Brew.

Contact Us - Safe and secure

To book us at your special function, please fill in your details below and we will respond to your query as soon as possible.

Name:

Company name:

Phone number:

Email address:

Question or comment: ( box )

Dapple Brew
Melbourne, Victoria, Australia
Info@dapplebrew.com.au
0471 925 164
Operating at your local function or event

Blog
Friendwall and Lensly integration.

Links

We have a heartfelt passionate and eternal pursuit for exceeding expectations, providing a memorable experience. It follows that we align ourselves with organizations, business's and people who also strive for perfection in what they do, providing great services, products and customer care.

Feel free to contact some of our contacts below who we have found to be above and beyond.

The Tamper Mill group - equipment suppliers

http://www.grindworks-supply.com.au

Kesi- barista consulting services

https://www.facebook.com/pages/Prime...Kesi/7301958264417086

Reedfinch Swimming Club

http://reedfinch.com.au/

Wexmoor Baseball Club

www.wexmoorfalcons.com.au/

Pellby Autos

http://www.pellbyautos.com.au

Target Market(s)

Lovers of Coffee at events and functions. Customers wanting coffee catered for at their event of function

Industry/Entity Type

Cafe

Font styles to use
Other font styles liked:
• La Chatte à Maman

Requirements
Must have
• Our logo design
• 5 pages but are open to any suggestions you think would benefit our development. We would also like to have links to our new Friendwall and Lensly pages on the bottom of each page.
Nice to have
• Your artistic flair and input

```html
<!DOCTYPE html>
<html lang="en">
<head>
<meta charset="utf-8">
<title>Dapple Brew</title>
<link rel="stylesheet" href="https://fonts.googleapis.com/css2?family=Roboto:wght@300;400;500;700&family=Yellowtail&display=swap">
<style>
:root{
  --accent:#e8380d;
  --ink:#222;
  --muted:#555;
  --white:#fff;
  --espresso:#2a1d15;
  --roast:#6e4a33;
  --night:#1c1c1c;
  --line:#9a9a9a;
}
*{box-sizing:border-box;margin:0;padding:0}
html,body{width:1200px;height:3256px;overflow:hidden}
body{position:relative;background:var(--white);font-family:"Roboto",sans-serif;color:var(--ink)}
section,header,footer{position:absolute;left:0;width:1200px}

.hero{top:0;height:680px;background:linear-gradient(160deg,#8a6a52 0%,#5a3d2b 40%,#3b2619 70%,#6d5442 100%);color:var(--white);text-align:center}
.hero-photo{position:absolute;inset:0;background:radial-gradient(ellipse at 62% 62%,rgba(240,232,220,.55) 0,rgba(240,232,220,0) 32%),radial-gradient(ellipse at 20% 30%,rgba(30,18,10,.5) 0,rgba(30,18,10,0) 45%)}
.main-nav{position:absolute;top:14px;left:84px;display:flex;gap:50px;font-size:17px;font-weight:500}
.social{position:absolute;top:20px;right:84px;display:flex;gap:40px}
.social span{display:block;width:22px;height:22px;background:rgba(255,255,255,.85);border-radius:3px}
.slide-arrow{position:absolute;top:235px;width:26px;height:56px;background:rgba(0,0,0,.55)}
.slide-arrow.prev{left:0}.slide-arrow.next{right:0}
.slide-arrow svg{position:absolute;top:20px;left:7px}
.brand-title{position:absolute;top:140px;width:100%;font-family:"Yellowtail",cursive;font-size:86px;font-weight:400}
.brand-mark{position:absolute;top:252px;left:550px;width:100px;height:100px;border-radius:50%;background:var(--night);display:flex;align-items:center;justify-content:center;font-size:15px;font-weight:500;color:var(--white);line-height:1.1}
.tagline{position:absolute;top:382px;width:100%;font-size:22px;font-weight:400}
.btn{display:inline-flex;align-items:center;justify-content:center;gap:14px;background:var(--accent);color:var(--white);font-size:20px;font-weight:400}
.hero .btn{position:absolute;top:496px;left:478px;width:244px;height:66px}

.divider-band{top:680px;height:40px;background:#4a4a4a}

.about{top:720px;height:520px;background:linear-gradient(100deg,#2c2c2c 0%,#3f3a36 45%,#5a524b 70%,#2f2d2b 100%);color:var(--white)}
.section-title{font-size:40px;font-weight:400;text-align:center}
.about .section-title{position:absolute;top:60px;width:100%}
.about-rule{position:absolute;top:122px;left:480px;width:240px;height:2px;background:rgba(255,255,255,.7)}
.about-copy{position:absolute;top:160px;left:88px;width:1024px;font-size:14.5px;line-height:24px;font-weight:500}
.about-copy p+p{margin-top:22px}
.about-sign{position:absolute;top:468px;right:92px;font-size:20px}

.blog{top:1240px;height:700px}
.blog .section-title{position:absolute;top:28px;width:100%;color:var(--ink)}
.blog-intro{position:absolute;top:84px;left:130px;width:940px;text-align:center;font-size:19px;line-height:28px;color:#333}
.post{position:absolute;left:88px;width:1072px;height:236px}
.post-1{top:168px}.post-2{top:432px}
.post-photo{position:absolute;left:0;top:0;width:532px;height:236px;background:radial-gradient(ellipse at 45% 48%,#f1ece4 0,#d9cbb8 18%,#5c3a22 40%,#2b170b 75%,#1a0e06 100%)}
.post-text{position:absolute;left:560px;top:4px;width:512px}
.post-title{font-size:25px;font-weight:400;color:var(--accent);margin-bottom:14px}
.post-body{font-size:14px;line-height:22.5px;color:#222}

.contact{top:1940px;height:768px}
.contact .section-title{position:absolute;top:24px;width:100%}
.title-rule{position:absolute;top:96px;left:416px;width:368px;height:12px}
.contact-intro{position:absolute;top:138px;left:300px;width:600px;text-align:center;font-size:15px;line-height:24px;color:#333}
.booking-form{position:absolute;top:270px;left:88px;width:532px}
.field{position:relative;height:80px;border-bottom:2px solid var(--line)}
.field label{position:absolute;left:0;bottom:10px;display:flex;align-items:center;gap:12px;font-size:17px;color:#222}
.field.active{border-bottom-color:var(--accent)}
.send{position:absolute;top:400px;left:0;width:216px;height:50px;font-size:22px}
.contact-info{position:absolute;top:262px;left:740px;width:420px}
.contact-info h3{font-size:40px;font-weight:300;color:#333;margin-bottom:28px}
.contact-info li{list-style:none;display:flex;align-items:center;gap:30px;height:60px;font-size:16px;color:#333}

.map{top:2708px;height:272px;background:linear-gradient(120deg,#dfe4d6 0%,#ece9e0 35%,#d6dccb 60%,#e6e2d8 100%)}
.map-pin{position:absolute;left:508px;top:66px}

.promo{top:2980px;height:212px;background:var(--roast);text-align:center;color:var(--white)}
.promo-line{position:absolute;top:42px;width:100%;font-family:"Yellowtail",cursive;font-size:54px}
.promo .btn{position:absolute;top:130px;left:504px;width:192px;height:52px;font-family:"Yellowtail",cursive;font-size:28px}

.site-footer{top:3192px;height:64px;background:var(--night);color:var(--white);font-size:15px}
.footer-nav{position:absolute;top:22px;left:84px;display:flex;gap:64px}
.copyright{position:absolute;top:22px;right:92px}
</style>
</head>
<body>

<header class="hero">
  <div class="hero-photo" role="img" aria-label="Photo of a cup of coffee on a saucer beside roasted coffee beans"></div>
  <nav class="main-nav"><span>Home</span><span>About</span><span>Contact Us</span><span>Blog</span></nav>
  <div class="social" aria-label="Social links"><span></span><span></span></div>
  <div class="slide-arrow prev"><svg width="12" height="16" viewBox="0 0 12 16"><path d="M10 1 3 8l7 7" fill="none" stroke="#fff" stroke-width="3"/></svg></div>
  <div class="slide-arrow next"><svg width="12" height="16" viewBox="0 0 12 16"><path d="M2 1l7 7-7 7" fill="none" stroke="#fff" stroke-width="3"/></svg></div>
  <h1 class="brand-title">Dapple Brew</h1>
  <div class="brand-mark">Dapple<br>Brew</div>
  <p class="tagline">Beautifully made coffee is a pleasure we should all enjoy at least once in our day.</p>
  <a class="btn">
    <svg width="30" height="20" viewBox="0 0 30 20"><path d="M1 10C6 2 24 2 29 10 24 18 6 18 1 10Z" fill="var(--night)"/><circle cx="15" cy="10" r="5" fill="var(--accent)"/><circle cx="15" cy="10" r="2.5" fill="var(--night)"/></svg>
    More Details
  </a>
</header>

<div class="divider-band" style="position:absolute;left:0;width:1200px"></div>

<section class="about">
  <div role="img" aria-label="Dark photo of a barista pouring coffee" style="position:absolute;inset:0;background:radial-gradient(ellipse at 70% 40%,rgba(200,190,180,.25) 0,rgba(0,0,0,0) 40%)"></div>
  <h2 class="section-title">About Us</h2>
  <div class="about-rule"></div>
  <div class="about-copy">
    <p>Served From our restored 1976 Roamvan we strive to provide you with an experience that will enhance your day. The care we show comes from years of training and experience as a Battista in several countries around the world. We trust the joy of our lovingly made coffee and our retro style service will linger. Serving great coffee at an event or function near you.</p>
    <p>Dapple brew believes in good old fashion retro service and a high a quality product. We care that our customers receive a beautifully made coffee, chai or hot chocolate. We serve our patrons with a heartfelt smile, aiming to enhance their day. We are fortunate enough to operate from our recently restored 1976 Roamvan at functions and events around Melbourne. You can follow us on Friendwall and Lensly or book us for you special function via our contact page. We look forward to wing able to serve you.</p>
  </div>
  <p class="about-sign">Dapple Brew</p>
</section>

<section class="blog">
  <h2 class="section-title">Blog</h2>
  <p class="blog-intro">Lorem Ipsum is simply dummy text of the printing and typesetting industry. Lorem Ipsum has been the industry's standard dummy text ever since the 1500s</p>
  <article class="post post-1">
    <div class="post-photo" role="img" aria-label="Photo of a white cup of black coffee among coffee beans"></div>
    <div class="post-text">
      <h3 class="post-title">Lorem Ipsum is simply dummy text of the</h3>
      <p class="post-body">Lorem Ipsum is simply dummy text of the printing and typesetting industry. Lorem Ipsum has been the industry's standard dummy text ever since the 1500s, when an unknown printer took a galley of type and scrambled it to make a type specimen book. It has survived not only five centuries, but also the leap into electronic typesetting, remaining essentially unchanged. It was popularised</p>
    </div>
  </article>
  <article class="post post-2">
    <div class="post-photo" role="img" aria-label="Photo of a white cup of black coffee among coffee beans"></div>
    <div class="post-text">
      <h3 class="post-title">Lorem Ipsum is simply dummy text of the</h3>
      <p class="post-body">Lorem Ipsum is simply dummy text of the printing and typesetting industry. Lorem Ipsum has been the industry's standard dummy text ever since the 1500s, when an unknown printer took a galley of type and scrambled it to make a type specimen book. It has survived not only five centuries, but also the leap into electronic typesetting, remaining essentially unchanged. It was popularised</p>
    </div>
  </article>
</section>

<section class="contact">
  <h2 class="section-title">Get in touch</h2>
  <svg class="title-rule" viewBox="0 0 368 12"><line x1="0" y1="6" x2="164" y2="6" stroke="#555" stroke-width="1.5"/><line x1="204" y1="6" x2="368" y2="6" stroke="#555" stroke-width="1.5"/><path d="M184 0l1.8 4h4.2l-3.4 2.6 1.3 4.4-3.9-2.7-3.9 2.7 1.3-4.4-3.4-2.6h4.2z" fill="var(--accent)"/></svg>
  <p class="contact-intro">To book us at your special function, please fill in your details below and we will respond to your query as soon as possible.</p>

  <form class="booking-form">
    <div class="field"><label><svg width="18" height="18" viewBox="0 0 18 18"><circle cx="9" cy="5" r="4" fill="#222"/><path d="M1 18c0-5 3.5-7 8-7s8 2 8 7z" fill="#222"/></svg>Name :</label></div>
    <div class="field"><label><svg width="20" height="18" viewBox="0 0 20 18"><path d="M2 17V7l8-5 8 5v10" fill="none" stroke="#222" stroke-width="2"/><rect x="7" y="10" width="6" height="7" fill="#222"/></svg>Company name:</label></div>
    <div class="field"><label><svg width="18" height="18" viewBox="0 0 18 18"><path d="M4 1l3 4-2 2c1 2.5 3.5 5 6 6l2-2 4 3-2 3C8 17 1 10 1 3z" fill="#222"/></svg>Phone number:</label></div>
    <div class="field"><label><svg width="20" height="14" viewBox="0 0 20 14"><rect x="1" y="1" width="18" height="12" fill="none" stroke="#222" stroke-width="2"/><path d="M1 1l9 7 9-7" fill="none" stroke="#222" stroke-width="2"/></svg>Email address:</label></div>
    <div class="field active"><label>Question or comment: &nbsp;( ...</label></div>
    <a class="btn send">Send</a>
  </form>

  <div class="contact-info">
    <h3>Contact info</h3>
    <ul>
      <li><svg width="22" height="20" viewBox="0 0 22 20"><path d="M11 1 1 10h3v9h5v-6h4v6h5v-9h3z" fill="#333"/></svg>Melbourne, Victoria, Australia</li>
      <li><svg width="22" height="16" viewBox="0 0 22 16"><rect x="1" y="1" width="20" height="14" fill="#333"/><path d="M1 1l10 8 10-8" fill="none" stroke="#fff" stroke-width="1.5"/></svg>Info@dapplebrew.com.au</li>
      <li><svg width="22" height="20" viewBox="0 0 18 18"><path d="M4 1l3 4-2 2c1 2.5 3.5 5 6 6l2-2 4 3-2 3C8 17 1 10 1 3z" fill="#333"/></svg>0471 925 164</li>
    </ul>
  </div>
</section>

<section class="map" role="img" aria-label="Street map of Melbourne with a location marker">
  <svg class="map-pin" width="24" height="34" viewBox="0 0 24 34"><path d="M12 33C5 22 1 17 1 11a11 11 0 0 1 22 0c0 6-4 11-11 22z" fill="var(--accent)"/><circle cx="12" cy="11" r="4" fill="#fff"/></svg>
</section>

<section class="promo">
  <p class="promo-line">all you need, give it a go</p>
  <a class="btn">More read</a>
</section>

<footer class="site-footer">
  <nav class="footer-nav"><span>Home</span><span>About</span><span>Contact Us</span><span>Blog</span></nav>
  <p class="copyright">@copyright 2015</p>
</footer>

</body>
</html>
```